Packaging and Insert Design for New Cocktail/Bar Set

We are launching a new product under our brand, Shakerly Guild, and require a design for the product packaging (2 packages - an inner cylinder tube and an outer box), as well as an insert.

(Note for reference - "mixology" is the art of cocktail making).

Our product is a cocktail set which will be sold on the USA Bazarro site.

Our logo has already been designed - please refer to the attached files. I've attached various vector files of our logo.

The cocktail set will be packaged in a cylinder tube box.
Please see uploaded files for an image of the cylinder, as well as dimensions.
Dimensions are 37.68cm x 28cm (when the print design is laid flat).
The physical tube will be 28cm high and have a diameter of 12cm.
See uploaded file 'Dimensions - Cylinder Box' for details.

The cylinder box will be enclosed in an outer white box for protection. The outer white box will be a very basic box (i.e. not high quality) we are using just to make storage of individual units easier (and to protect the cylinder tube). It is unlikely that the outer box will be retained by the buyer. It will have a very clean, simple design. It will have our logo on the front and a barcode on the back (at the bottom).
Dimensions of the outer box are 28.5cm high and 12.5cm wide (tall and rectangular in shape).
See uploaded file 'Dimensions - White Outer Box & Paper Card' for details.

So to confirm we have 2 packages - the internal cylinder tube will have full branding, and this will then be placed in the white outer box with a simple design (logo only plus barcode at the back).

We also require a small insert to be designed (9.1cm x 5.5cm). We will include the insert in the package. The insert will have our logo and will provide the buyer with our contact details. The buyer will register their email address with us, in order to quality for warranty and a free e-book.

We need to finalise the content for the product insert, as well as the additional information to be printed on the cylinder tube.

In terms of design for the inner cylinder tube, we are leaning towards a more simple design, with our logo displayed on the front of the box.
We are open to ideas/suggestions though.

We have also uploaded an image of the cocktail set components which will form part of the set.

Target Market(s)

Our target market will be cocktail making enthusiasts/hobbyists and professionals. This includes people who would like to but a cocktail set to use at home, as well as professional bartenders.

Industry/Entity Type

Product

Colors

Designer to choose colors to be used in the design.

Requirements
Must have
• Preference is for a clean, professional looking design.
• Internal cylinder tube - full branding, incorporating logo on the front. Possibly also either a slogan e.g. "The Art of Cocktail Making' or details of the product e.g. "Cocktail Making Set' or similar.
• Outer white box - very simple design with logo to be displayed on the front of the packaging.
Should not have
• The design should not be too busy/complex. Not too much going on.

```html
<!DOCTYPE html>
<html lang="en">
<head>
<meta charset="utf-8">
<title>Shakerly Guild – Cocktail Making Set Packaging</title>
<link href="https://fonts.googleapis.com/css2?family=Alfa+Slab+One&family=Oswald:wght@600&family=Rye&family=Montserrat:wght@300;400;800&family=Roboto+Condensed:wght@500&display=swap" rel="stylesheet">
<style>
  :root {
    --page: #f1f1f1;
    --steel-light: #e4e4e6;
    --steel-mid: #c4c5c8;
    --steel-dark: #a9aaae;
    --ink: #1c1d20;
    --tube-black: #1b1d20;
    --tube-navy: #1d2a36;
    --label-blue: #2a8ec9;
    --label-deep: #13557d;
    --copper: #d98a4a;
    --copper-light: #f0ad6e;
    --title-blue: #3aa6dd;
    --brand-blue: #4f93c4;
    --white: #f4f4f4;
  }
  * { margin: 0; padding: 0; box-sizing: border-box; }
  html, body { width: 1084px; height: 1200px; overflow: hidden; }
  body { background: var(--page); position: relative; font-family: "Montserrat", sans-serif; }

  /* Outer box front panel */
  .outer-box {
    position: absolute; left: 138px; top: 112px; width: 350px; height: 978px;
    background:
      repeating-linear-gradient(180deg, rgba(255,255,255,.18) 0 1px, rgba(0,0,0,.03) 1px 3px),
      linear-gradient(90deg, var(--steel-mid) 0%, var(--steel-light) 45%, var(--steel-mid) 75%, var(--steel-dark) 100%);
  }
  .outer-box .brand-vertical {
    position: absolute; left: 166px; top: 214px;
    writing-mode: vertical-rl;
    font-family: "Montserrat", sans-serif; font-weight: 400;
    font-size: 17px; letter-spacing: 4px; line-height: 1; color: var(--ink);
    display: flex; align-items: center; gap: 10px;
    white-space: nowrap;
  }
  .outer-box .brand-vertical .dot {
    width: 11px; height: 11px; border-radius: 50%; background: var(--ink);
  }
  .outer-box .divider {
    position: absolute; left: 146px; top: 496px; width: 56px; height: 2px; background: var(--label-blue);
  }
  .outer-box .slogan {
    position: absolute; left: 160px; top: 524px;
    writing-mode: vertical-rl;
    font-family: "Roboto Condensed", sans-serif; font-weight: 500;
    font-size: 27px; line-height: 1; color: var(--ink); white-space: nowrap;
  }

  /* Cylinder wrap, laid flat */
  .tube-wrap {
    position: absolute; left: 621px; top: 124px; width: 305px; height: 952px;
    background: linear-gradient(90deg, #141618 0%, var(--tube-black) 40%, #2a2d31 70%, #141618 100%);
  }
  .tube-wrap .frame { position: absolute; left: 0; top: 0; }

  .made-in {
    position: absolute; left: 0; width: 305px; top: 84px; text-align: center;
    font-family: "Rye", serif; font-size: 19px; line-height: 1; color: var(--copper);
  }
  .country {
    position: absolute; left: 0; width: 305px; top: 114px; text-align: center;
    font-family: "Oswald", sans-serif; font-weight: 600; font-size: 34px; line-height: 1.1;
    letter-spacing: 1px; color: var(--copper-light); white-space: nowrap;
  }
  .scene-top, .scene-bottom {
    position: absolute; left: 40px; width: 225px;
    background: linear-gradient(180deg, #2f7fb0 0%, var(--label-deep) 100%);
  }
  .scene-top { top: 168px; height: 144px; }
  .scene-bottom { top: 716px; height: 160px; }

  .title-plaque {
    position: absolute; left: 15px; top: 312px; width: 276px; height: 152px;
    background: var(--tube-navy); border: 4px solid var(--copper); border-radius: 10px;
    display: flex; flex-direction: column; align-items: center; justify-content: center;
    font-family: "Alfa Slab One", serif; color: var(--title-blue); line-height: 1;
    overflow: hidden;
  }
  .title-plaque span { display: block; white-space: nowrap; transform: scaleX(0.76); }
  .title-plaque .line1 { font-size: 46px; }
  .title-plaque .line2 { font-size: 36px; margin-top: 6px; }

  .maker-tag {
    position: absolute; left: 75px; top: 468px; width: 172px; height: 26px;
    background: var(--label-blue); color: var(--tube-navy);
    font-family: "Montserrat", sans-serif; font-weight: 800; font-size: 13px;
    display: flex; align-items: center; justify-content: center; white-space: nowrap;
  }
  .brand-name {
    position: absolute; left: 0; width: 305px; top: 572px;
    display: flex; align-items: center; justify-content: center; gap: 10px;
    font-family: "Montserrat", sans-serif; font-weight: 400;
    font-size: 18px; letter-spacing: 4px; line-height: 1; color: var(--brand-blue);
    white-space: nowrap;
  }
  .brand-name .dot { width: 10px; height: 10px; border-radius: 50%; background: var(--brand-blue); }
  .claim {
    position: absolute; left: 0; width: 305px; top: 638px; text-align: center;
    font-family: "Montserrat", sans-serif; font-weight: 800; font-size: 38px;
    letter-spacing: -1px; color: var(--white); line-height: 1; white-space: nowrap;
  }
  .material {
    position: absolute; left: 0; width: 305px; top: 686px; text-align: center;
    font-family: "Montserrat", sans-serif; font-weight: 300; font-size: 22px;
    letter-spacing: 4px; line-height: 1; color: var(--white); white-space: nowrap;
  }
</style>
</head>
<body>

  <section class="outer-box" aria-label="Outer box front">
    <div class="brand-vertical"><span class="dot"></span>SHAKERLY GUILD</div>
    <div class="divider"></div>
    <div class="slogan">The Art of Cocktail Making</div>
  </section>

  <section class="tube-wrap" aria-label="Cylinder tube label">
    <svg class="frame" width="305" height="952" viewBox="0 0 305 952" aria-hidden="true">
      <path d="M28 898 L28 130 Q28 110 48 110 L48 100 Q48 72 80 72 L100 72 Q110 58 130 58 L175 58 Q195 58 205 72 L225 72 Q257 72 257 100 L257 110 Q277 110 277 130 L277 898 Z"
            fill="var(--tube-navy)" stroke="var(--label-blue)" stroke-width="6"/>
      <path d="M36 890 L36 134 Q36 118 54 118 L56 118 L56 104 Q56 80 82 80 L104 80 Q114 66 132 66 L173 66 Q191 66 201 80 L223 80 Q249 80 249 104 L249 118 L251 118 Q269 118 269 134 L269 890 Z"
            fill="none" stroke="var(--label-deep)" stroke-width="2"/>
    </svg>

    <div class="made-in">-MADE IN-</div>
    <div class="country">COUNTRY NAME</div>

    <div class="scene-top" role="img" aria-label="Vintage engraved bar scene with a pouring bottle and three cocktail glasses"></div>

    <div class="title-plaque">
      <span class="line1">COCKTAIL</span>
      <span class="line2">MAKING SET</span>
    </div>

    <div class="maker-tag">MANUFATURED BY</div>
    <div class="brand-name"><span class="dot"></span>SHAKERLY GUILD</div>

    <div class="claim">TOXIC FREE</div>
    <div class="material">stainless steel</div>

    <div class="scene-bottom" role="img" aria-label="Vintage engraved saloon interior with a hanging chandelier"></div>
  </section>

</body>
</html>
```